environmentalist needs a bumper sticker design

The bumper sticker should say, "There is no Planet B."

thank you for the designs so far. Some have asked for more direction of my thinking. You've probably heard people talk of "Plan A" and "Plan B" when they want to consider alternatives. "There is no Planet B" reminds us that there are no alternatives. The question is, how best to encourage people to act? Research indicates that making people fearful is less effective (although certainly we have plenty to fear). It is more effective to stir emotions of caring and attachment. For example, designs that show the earth as a beautiful planet, or aspects of the earth (e.g., trees and mountains or whatever) remind us of what we love and want to care for.

```html
<!DOCTYPE html>
<html lang="en">
<head>
<meta charset="utf-8">
<title>There Is No Planet B – Bumper Sticker</title>
<link rel="stylesheet" href="https://fonts.googleapis.com/css2?family=Titan+One&display=swap">
<style>
  :root {
    --sticker-green: #8ebf1f;
    --smoke-dark: #3a3a3a;
    --smoke-edge: #d6d6d6;
    --earth-ocean: #3f7f8f;
    --earth-land: #4f9a5a;
    --smoke-ring: #6a6a6a;
  }
  html, body {
    margin: 0;
    padding: 0;
    overflow: hidden;
    background: var(--sticker-green);
  }
  .sticker {
    position: relative;
    width: 1200px;
    height: 302px;
    background: var(--sticker-green);
    overflow: hidden;
  }
  .earth-illustration {
    position: absolute;
    left: 38px;
    top: 6px;
    width: 292px;
    height: 292px;
    border-radius: 50%;
    background:
      radial-gradient(circle at 50% 50%,
        var(--earth-land) 0%,
        var(--earth-ocean) 38%,
        var(--earth-ocean) 44%,
        var(--sticker-green) 47%,
        var(--sticker-green) 55%,
        var(--smoke-ring) 58%,
        var(--smoke-ring) 64%,
        var(--sticker-green) 67%);
  }
  .slogan {
    position: absolute;
    left: 350px;
    top: 14px;
    width: 790px;
    height: 276px;
  }
  .slogan-line {
    font-family: "Titan One", sans-serif;
    fill: var(--smoke-dark);
    stroke: var(--smoke-edge);
    stroke-width: 5px;
    paint-order: stroke fill;
    stroke-linejoin: round;
  }
  .slogan-line--top { font-size: 112px; }
  .slogan-line--bottom { font-size: 132px; }
</style>
</head>
<body>
  <main class="sticker">
    <div class="earth-illustration" role="img"
         aria-label="Illustration of an angry planet Earth surrounded by a ring of dark smoke and factory chimneys"></div>

    <svg class="slogan" viewBox="0 0 790 276" role="img" aria-label="There is no Planet B">
      <text class="slogan-line slogan-line--top" x="10" y="108"
            textLength="770" lengthAdjust="spacingAndGlyphs">THERE IS NO</text>
      <text class="slogan-line slogan-line--bottom" x="40" y="256"
            textLength="740" lengthAdjust="spacingAndGlyphs">PLANET B</text>
    </svg>
  </main>
</body>
</html>
```